Industrial Automation company requires a business card design

Valtrin Automation provides design & build of Automated Equipment for manufacturing industry.
www.valtrinautomation.example
The equipment we design is used for manufacturing in sectors such as medical device, pharmaceutical, aerospace and electronics.
We require a new business card design which incorporates our (New) logo and the key message words:
Automated Equipment:
Design, Build, Control, Test, Support

```html
<!DOCTYPE html>
<html lang="en">
<head>
<meta charset="utf-8">
<title>Valtrin Automation – Business Card, Draft 02</title>
<link rel="stylesheet" href="https://fonts.googleapis.com/css2?family=Montserrat:wght@500;600;800&display=swap">
<style>
  :root {
    --green: #0b7a3e;
    --green-dark: #08703a;
    --green-band: #14874a;
    --brand-green: #0e8040;
    --white: #ffffff;
    --ink: #1b1b1b;
    --frame: #8a8a8a;
    --font: "Montserrat", Arial, sans-serif;
  }
  * { box-sizing: border-box; margin: 0; padding: 0; }
  html, body { width: 1200px; height: 410px; overflow: hidden; background: var(--white); }
  body { position: relative; font-family: var(--font); color: var(--ink); }

  .card { position: absolute; top: 37px; width: 531px; height: 295px; overflow: hidden; }

  /* Front */
  .card--front { left: 25px; background: var(--green-dark); }
  .card--front .card__bands { position: absolute; inset: 0; }
  .front__wordmark {
    position: absolute; left: 0; top: 97px; width: 372px; height: 100px;
  }
  .front__wordmark svg { position: absolute; inset: 0; }
  .wordmark {
    position: absolute; display: flex; align-items: center; gap: 8px;
    color: var(--brand-green); font-weight: 800; text-transform: uppercase;
    letter-spacing: 0.5px; white-space: nowrap;
  }
  .front__wordmark .wordmark { left: 34px; top: 38px; font-size: 19px; }
  .wordmark__dot { width: 12px; height: 12px; border-radius: 50%; background: var(--brand-green); flex: none; }
  .front__person {
    position: absolute; right: 24px; top: 128px; text-align: right; color: var(--white);
    white-space: nowrap;
  }
  .person__name { font-size: 16px; font-weight: 600; line-height: 20px; }
  .person__role { font-size: 12px; }
  .person__email { font-size: 13.5px; font-weight: 500; line-height: 20px; }

  /* Back */
  .card--back { left: 617px; width: 532px; background: var(--white); border: 1px solid var(--frame); }
  .card--back .wordmark { left: 86px; top: 65px; font-size: 22px; }
  .contact-list { position: absolute; left: 86px; top: 116px; list-style: none; }
  .contact-list li {
    display: flex; align-items: center; gap: 8px; white-space: nowrap;
    height: 23px; font-size: 15px; font-weight: 500; color: var(--ink);
  }
  .contact-list svg { width: 14px; height: 14px; fill: var(--green); flex: none; }

  .draft-label { position: absolute; left: 35px; top: 352px; font-size: 15px; font-weight: 500; }
</style>
</head>
<body>

<section class="card card--front" aria-label="Card front">
  <svg class="card__bands" viewBox="0 0 531 295" preserveAspectRatio="none" aria-hidden="true">
    <rect width="531" height="295" fill="var(--green-dark)"/>
    <path d="M0 0 H380 C300 60 220 90 0 95 Z" fill="var(--green)"/>
    <path d="M380 0 H531 V70 C470 60 420 30 400 0 Z" fill="var(--green-band)"/>
    <path d="M420 0 H500 C520 80 531 160 531 295 H470 C500 200 480 90 420 0 Z" fill="var(--green-band)" opacity="0.7"/>
    <path d="M60 200 C200 230 330 240 531 215 V295 H260 C330 270 200 240 60 200 Z" fill="var(--green-band)"/>
    <path d="M120 295 C260 260 420 255 531 262 V295 Z" fill="var(--green)"/>
  </svg>
  <div class="front__wordmark">
    <svg viewBox="0 0 372 100" preserveAspectRatio="none" aria-hidden="true">
      <polygon points="0,0 290,0 372,100 0,100" fill="var(--white)"/>
    </svg>
    <div class="wordmark"><span class="wordmark__dot"></span>Valtrin Automation</div>
  </div>
  <div class="front__person">
    <p class="person__name">YOUR NAME <span class="person__role">(CEO)</span></p>
    <p class="person__email">name@valtrin.example</p>
  </div>
</section>

<section class="card card--back" aria-label="Card back">
  <div class="wordmark">Valtrin Automation</div>
  <ul class="contact-list">
    <li>
      <svg viewBox="0 0 14 14" aria-hidden="true"><path d="M7 0a5 5 0 0 0-5 5c0 3.6 5 9 5 9s5-5.4 5-9a5 5 0 0 0-5-5zm0 7a2 2 0 1 1 0-4 2 2 0 0 1 0 4z"/></svg>
      Kilbrannagh, Dunmara, Co. Cork, Ireland
    </li>
    <li>
      <svg viewBox="0 0 14 14" aria-hidden="true"><path d="M3 1l2.5 3-1.3 1.5c.8 1.7 2.1 3 3.8 3.8L9.5 8 12.5 10.5 11 13C5.5 12.6 1.4 8.5 1 3z"/></svg>
      00 353 (0) 21 55140
    </li>
    <li>
      <svg viewBox="0 0 14 14" aria-hidden="true"><path d="M3 1h8v3H3zM1 5h12v6h-2V9H3v2H1zM4 10h6v3H4z"/></svg>
      00 353 (0) 21 55150
    </li>
    <li>
      <svg viewBox="0 0 14 14" aria-hidden="true"><path d="M1 3h12v8H1zM1.5 3.5 7 8l5.5-4.5" stroke="var(--white)" stroke-width="1"/></svg>
      mward@valtrin.example | info@valtrin.example
    </li>
    <li>
      <svg viewBox="0 0 14 14" aria-hidden="true"><circle cx="7" cy="7" r="6"/><path d="M1 7h12M7 1c-3 3-3 9 0 12M7 1c3 3 3 9 0 12M2 4h10M2 10h10" stroke="var(--white)" stroke-width="0.9" fill="none"/></svg>
      www.valtrinautomation.example
    </li>
  </ul>
</section>

<p class="draft-label">Draft 02</p>

</body>
</html>
```